Flyer Tally Your Ledger Free

Hi
Can you please design me a DL Flyer for: Tally Your Ledger Free
Info:
Starting a new Business ?
Want to save on bookkeeping fees for your existing business?

You can now save 1000's off bookkeeping fees by Doing it Yourself.

Using our Bookkeeper software you simply key in the information as you go.

We offer one on one training, backup and support.
We can assist you with BAS Preparation and Payrol Advice.

Add Modules as required:
Point of Sale Module
Jobs Management Module
Website Intergration Module

Fee set up assistance and training.

Lets get the ball rolling: 1300 642 815
www.tylfr.com.au
admin@tylfr.com.au (use the logo thing you made)

Target Market(s)

Small Business

Colors
ec1f27
f04a50
f59296
fcdcdc
ffffff

Requirements
Nice to have
• image/s related to bookkeeping

```html
<!DOCTYPE html>
<html lang="en">
<head>
<meta charset="utf-8">
<title>Tally Your Ledger Free – DL Flyer</title>
<link rel="stylesheet" href="https://fonts.googleapis.com/css2?family=Roboto:wght@300;400;500;700;900&family=Roboto+Condensed:wght@400;700&display=swap">
<style>
  :root{
    --red:#ec1f27;
    --red-soft:#f04a50;
    --pink:#f59296;
    --blush:#fcdcdc;
    --white:#ffffff;
    --charcoal:#45403d;
    --ink:#3a3634;
    --stage:#b3b3b3;
  }
  *{box-sizing:border-box;margin:0;padding:0}
  html,body{width:1200px;height:1200px;overflow:hidden;background:var(--stage)}
  body{position:relative;font-family:"Roboto",sans-serif}
  .flyer{position:absolute;top:160px;width:440px;height:880px;overflow:hidden}
  .flyer--front{left:130px;background:var(--charcoal)}
  .flyer--back{left:630px;background:var(--white)}
  .abs{position:absolute}
  svg.shapes{position:absolute;left:0;top:0}

  /* front */
  .photo{left:0;top:0;width:440px;height:420px;
    background:linear-gradient(160deg,#f4efe6 0%,#e6ddd0 30%,#b9c3cc 60%,#4e5a6a 100%)}
  .brand{left:0;top:58px;width:440px;display:flex;justify-content:center;align-items:center;gap:10px}
  .brand__dot{width:26px;height:26px;border-radius:50%;background:var(--red)}
  .brand__name{font-family:"Roboto",sans-serif;font-weight:500;font-size:27px;color:var(--red)}
  .lead{left:36px;top:424px;font-weight:300;font-size:34px;color:var(--blush);letter-spacing:.5px}
  .headline{left:36px;top:462px;font-weight:700;font-size:44px;color:var(--white)}
  .question{left:36px;top:529px;width:363px;height:57px;background:var(--blush);
    font-family:"Roboto Condensed",sans-serif;font-weight:700;font-size:15.5px;color:var(--ink);
    padding:9px 13px;line-height:1.35}
  .saving{left:40px;top:606px;width:358px;height:188px;border:1.5px solid var(--blush)}
  .saving__head{height:36px;background:var(--pink);text-align:center;
    font-family:"Roboto Condensed",sans-serif;font-size:26px;color:var(--ink);line-height:36px}
  .saving__amount{left:10px;top:38px;font-family:"Roboto Condensed",sans-serif;font-weight:700;
    font-size:104px;color:var(--white);line-height:1;letter-spacing:-2px}
  .saving__off{left:322px;top:52px;width:30px;writing-mode:vertical-rl;
    font-family:"Roboto Condensed",sans-serif;font-weight:700;font-size:32px;color:var(--white);letter-spacing:1px}
  .saving__note{left:0;top:150px;width:356px;text-align:center;
    font-family:"Roboto Condensed",sans-serif;font-size:15px;color:var(--white)}
  .footer-front{left:0;top:800px;width:440px;height:80px;background:var(--red);border-top:4px solid var(--white);
    text-align:center;color:var(--white);font-weight:700;font-size:17px;line-height:26px;padding-top:12px}

  /* back */
  .offer{left:0;top:44px;width:440px;text-align:center;font-weight:400;font-size:25px;color:var(--blush);letter-spacing:1px}
  .training{left:0;top:76px;width:440px;text-align:center;font-weight:900;font-size:74px;color:var(--white);letter-spacing:1px}
  .support{left:0;top:168px;width:440px;text-align:center;font-weight:400;font-size:25px;color:var(--blush);letter-spacing:1px}
  .assist{left:30px;top:365px;width:380px;text-align:center;font-weight:700;font-size:16px;line-height:1.35;color:var(--ink)}
  .modules-banner{left:22px;top:420px;width:396px;height:40px;background:var(--red-soft);
    color:var(--white);font-weight:700;font-size:21px;line-height:40px;text-align:center;letter-spacing:.5px}
  .module{width:130px;text-align:center;top:556px;font-weight:700;font-size:15px;line-height:1.25;color:var(--ink)}
  .fee{left:30px;top:636px;font-weight:900;font-size:128px;line-height:1;color:var(--red);letter-spacing:-3px}
  .fee-setup{left:300px;top:640px;writing-mode:vertical-rl;transform:rotate(180deg);
    font-weight:900;font-size:34px;color:var(--ink);letter-spacing:1px}
  .assist-bar{left:22px;top:758px;width:300px;height:34px;background:var(--charcoal);
    color:var(--white);font-weight:700;font-size:16px;line-height:34px;padding-left:16px;letter-spacing:.5px}
  .footer-back{left:0;top:792px;width:440px;height:88px;background:var(--red);
    color:var(--white);font-weight:700;font-size:22px;line-height:32px;padding:12px 0 0 60px}
</style>
</head>
<body>

<section class="flyer flyer--front" aria-label="Flyer front">
  <div class="abs photo" role="img" aria-label="Photograph of hands working on financial papers with a pen, calculator and tablet on an office desk"></div>
  <svg class="shapes" width="440" height="440" viewBox="0 0 440 440" aria-hidden="true">
    <polygon points="220,378 290,352 420,372 298,405" fill="var(--red)"/>
    <polyline points="0,384 102,322 298,404 440,352" fill="none" stroke="var(--white)" stroke-width="5"/>
    <polygon points="0,392 102,331 298,412 440,362 440,440 0,440" fill="var(--charcoal)"/>
  </svg>
  <div class="abs brand"><span class="brand__dot"></span><span class="brand__name">Tally Your Ledger Free</span></div>

  <p class="abs lead">STARTING A</p>
  <h1 class="abs headline">NEW BUSINESS?</h1>
  <p class="abs question">WANT TO SAVE ON BOOKKEEPING FEES FOR YOUR EXISTING BUSINESS?</p>

  <div class="abs saving">
    <div class="saving__head">YOU CAN NOW SAVE</div>
    <div class="abs saving__amount">1000’S</div>
    <div class="abs saving__off">OFF</div>
    <div class="abs saving__note">BOOKKEEPING FEES BY DOING IT YOURSELF</div>
  </div>

  <div class="abs footer-front">
    Lets get the ball rolling: 1300 642 815<br>www.tylfr.com.au
  </div>
</section>

<section class="flyer flyer--back" aria-label="Flyer back">
  <svg class="shapes" width="440" height="360" viewBox="0 0 440 360" aria-hidden="true">
    <polygon points="0,0 440,0 440,332 300,272 150,345 0,284" fill="var(--charcoal)"/>
    <polygon points="0,296 0,342 62,320" fill="var(--red)"/>
    <polygon points="190,322 300,282 440,342 440,352 330,346" fill="var(--red)"/>
    <polyline points="0,290 150,352 300,280 440,340" fill="none" stroke="var(--white)" stroke-width="4"/>
  </svg>
  <p class="abs offer">WE OFFER ONE ON ONE</p>
  <h2 class="abs training">TRAINING</h2>
  <p class="abs support">BACKUP AND SUPPORT</p>

  <p class="abs assist">WE CAN ASSIST YOU WITH BAS PREPARATION AND PAYROL ADVICE.</p>
  <div class="abs modules-banner">ADD MODULES AS REQUIRED:</div>

  <svg class="shapes" width="440" height="560" viewBox="0 0 440 560" aria-hidden="true">
    <line x1="85" y1="510" x2="355" y2="510" stroke="var(--charcoal)" stroke-width="3"/>
    <g fill="var(--charcoal)"><circle cx="85" cy="510" r="36"/><circle cx="220" cy="510" r="36"/><circle cx="355" cy="510" r="36"/></g>
    <g fill="none" stroke="var(--white)" stroke-width="2" stroke-linejoin="round" stroke-linecap="round">
      <rect x="75" y="488" width="20" height="20"/>
      <path d="M80 492 q5 7 10 0"/>
      <path d="M64 518 l10 -4 h14 l12 -6 l4 4 l-16 12 h-18"/>
      <circle cx="220" cy="510" r="9"/>
      <path d="M220 494 v-4 M220 526 v4 M204 510 h-4 M236 510 h4 M209 499 l-3 -3 M231 521 l3 3 M231 499 l3 -3 M209 521 l-3 3"/>
      <circle cx="355" cy="510" r="18"/>
      <ellipse cx="355" cy="510" rx="8" ry="18"/>
      <path d="M337 510 h36 M340 500 h30 M340 520 h30"/>
    </g>
  </svg>
  <p class="abs module" style="left:20px">Point of Sale<br>Module</p>
  <p class="abs module" style="left:155px">Jobs<br>Management<br>Module</p>
  <p class="abs module" style="left:290px">Website<br>Intergration<br>Module</p>

  <div class="abs fee">FEE</div>
  <div class="abs fee-setup">SETUP</div>
  <div class="abs assist-bar">ASSISTANCE AND TRAINING..</div>

  <div class="abs footer-back">admin@tylfr.com.au<br>www.tylfr.com.au</div>
</section>

</body>
</html>
```